Business Card (I don't have a logo)

I'm bootstrapping a new venture and need a business card and "look" for it. I'd like to print one side only, but could do a bleed to the edges, but don't need to. See my website: www.calebharrowpartners.example to get a sense of the photos that relate to the look/feel of my company.

Target Market(s)

high tech start-up company CEO's in Silicon Valley

Industry/Entity Type

Business

Requirements
Must have
• a look that can cut/paste onto my website that integrates easily with the front page photo. see www.calebharrowpartners.example

```html
<!DOCTYPE html>
<html lang="en">
<head>
<meta charset="utf-8">
<title>Caleb Harrow Partners — Business Cards</title>
<link rel="stylesheet" href="https://fonts.googleapis.com/css2?family=Federo&display=swap">
<style>
  :root {
    --backdrop: #e6e6e6;
    --card-white: #fffdf6;
    --ink: #111111;
    --mark-grey: #4a4a4a;
    --gold-deep: #c98a12;
    --gold: #e9b631;
    --gold-light: #f7dc7a;
    --cream: #fff6d8;
    --ember: #d9542a;
  }
  * { box-sizing: border-box; margin: 0; padding: 0; }
  html, body {
    width: 1200px;
    height: 328px;
    overflow: hidden;
    background: var(--backdrop);
  }
  .sheet {
    position: relative;
    width: 1200px;
    height: 328px;
  }
  .card {
    position: absolute;
    overflow: hidden;
    background: var(--card-white);
  }
  .card--portrait-art {
    left: 14px; top: 14px; width: 541px; height: 303px;
  }
  .card--landscape-art {
    left: 645px; top: 18px; width: 543px; height: 298px;
  }
  .artwork {
    position: absolute;
    inset: 0;
  }
  .card--portrait-art .artwork {
    background:
      radial-gradient(ellipse 120px 260px at 60px 150px, rgba(201,138,18,0.85), rgba(201,138,18,0) 70%),
      radial-gradient(ellipse 60px 120px at 150px 40px, rgba(217,84,42,0.25), rgba(217,84,42,0) 70%),
      linear-gradient(90deg, var(--gold-deep) 0%, var(--gold) 14%, var(--gold-light) 26%, var(--cream) 40%, var(--card-white) 58%);
  }
  .card--landscape-art .artwork {
    background:
      radial-gradient(ellipse 300px 90px at 380px 250px, rgba(201,138,18,0.8), rgba(201,138,18,0) 70%),
      radial-gradient(ellipse 260px 60px at 160px 200px, rgba(217,84,42,0.22), rgba(217,84,42,0) 70%),
      linear-gradient(180deg, var(--card-white) 0%, var(--card-white) 42%, var(--cream) 56%, var(--gold-light) 72%, var(--gold) 88%, var(--gold-deep) 100%);
  }
  .brand-mark {
    position: absolute;
    font-family: "Federo", sans-serif;
    color: var(--mark-grey);
    letter-spacing: 2px;
    line-height: 1;
  }
  .card--portrait-art .brand-mark { left: 300px; top: 80px; font-size: 52px; }
  .card--landscape-art .brand-mark { left: 32px; top: 88px; font-size: 56px; }
  .wordmark {
    position: absolute;
    font-family: "Federo", sans-serif;
    color: var(--ink);
    text-transform: uppercase;
    line-height: 1;
  }
  .wordmark__top {
    display: block;
    letter-spacing: 5px;
  }
  .wordmark__bottom {
    display: block;
    letter-spacing: 4px;
  }
  .card--portrait-art .wordmark { left: 220px; top: 186px; }
  .card--portrait-art .wordmark__top { font-size: 32px; }
  .card--portrait-art .wordmark__bottom { font-size: 56px; margin-top: 4px; }
  .card--landscape-art .wordmark { left: 232px; top: 30px; }
  .card--landscape-art .wordmark__top { font-size: 32px; }
  .card--landscape-art .wordmark__bottom { font-size: 58px; margin-top: 4px; }
</style>
</head>
<body>
  <main class="sheet">
    <section class="card card--portrait-art">
      <div class="artwork" role="img" aria-label="Abstract flowing gold and amber light swirls along the left edge"></div>
      <div class="brand-mark">CHP</div>
      <h1 class="wordmark">
        <span class="wordmark__top">Caleb Harrow</span>
        <span class="wordmark__bottom">Partners</span>
      </h1>
    </section>

    <section class="card card--landscape-art">
      <div class="artwork" role="img" aria-label="Abstract flowing gold and amber light waves across the lower half"></div>
      <div class="brand-mark">CHP</div>
      <h2 class="wordmark">
        <span class="wordmark__top">Caleb Harrow</span>
        <span class="wordmark__bottom">Partners</span>
      </h2>
    </section>
  </main>
</body>
</html>
```